Letterhead and envelope design

Using current logo and colours I would like to have a new design done for a stationary set to be printed.

The new files should include logo, web and email address as well as,mailing address and phone number

Dov Harmsby
Harmsby Construction Inc
Box 27 Site 18 RR5
Ridgeholt WL
T4K 2B9
Cell : 403-555-2917
Email: dov@harmsbyconstruction.example
web: harmsbyconstruction.example

```html
<!DOCTYPE html>
<html lang="en">
<head>
<meta charset="utf-8">
<title>Harmsby Construction – Envelope Set</title>
<link href="https://fonts.googleapis.com/css2?family=Roboto:wght@400;700&display=swap" rel="stylesheet">
<style>
  :root {
    --navy: #1b365d;
    --orange: #c87a1e;
    --backdrop: #e6e6e6;
    --paper: #f3f3f3;
    --ink-grey: #4a4a4a;
    --watermark: #d9dce1;
  }
  html, body {
    margin: 0;
    padding: 0;
    overflow: hidden;
  }
  body {
    width: 1200px;
    height: 795px;
    background: var(--backdrop);
    position: relative;
    font-family: "Roboto", Arial, sans-serif;
  }
  .envelope {
    position: absolute;
    width: 540px;
    height: 270px;
    background: var(--paper);
    box-shadow: 0 2px 6px rgba(0,0,0,0.12);
    overflow: hidden;
  }
  .envelope-front {
    left: 50px;
    top: 420px;
  }
  .envelope-front .watermark {
    position: absolute;
    right: -40px;
    bottom: -70px;
    width: 250px;
    height: 250px;
    border-radius: 50%;
    background: var(--watermark);
  }
  .brand {
    position: absolute;
    left: 30px;
    top: 24px;
    display: flex;
    align-items: center;
    gap: 10px;
  }
  .brand-dot {
    width: 40px;
    height: 40px;
    border-radius: 50%;
    background: var(--navy);
  }
  .brand-name {
    color: var(--navy);
    font-weight: 700;
    font-size: 13px;
    line-height: 1.15;
    letter-spacing: 0.5px;
  }
  .return-address {
    position: absolute;
    left: 30px;
    top: 92px;
    font-size: 9.5px;
    line-height: 1.35;
    font-style: normal;
    color: var(--ink-grey);
  }
  .return-address .company {
    color: var(--navy);
    font-weight: 700;
  }
  .front-stripe-accent {
    position: absolute;
    left: 0;
    right: 0;
    bottom: 26px;
    height: 3px;
    background: var(--orange);
  }
  .front-stripe-band {
    position: absolute;
    left: 0;
    right: 0;
    bottom: 0;
    height: 20px;
    background: var(--navy);
  }
  .envelope-back {
    left: 610px;
    top: 110px;
  }
  .envelope-back svg {
    position: absolute;
    inset: 0;
  }
</style>
</head>
<body>

  <section class="envelope envelope-front" aria-label="Envelope front">
    <div class="watermark"></div>
    <div class="brand">
      <div class="brand-dot"></div>
      <div class="brand-name">HARMSBY<br>CONSTRUCTION</div>
    </div>
    <address class="return-address">
      <span class="company">Harmsby Construction Inc</span><br>
      Box 27 Site 18 RR5<br>
      Ridgeholt WL T4K 2B9
    </address>
    <div class="front-stripe-accent"></div>
    <div class="front-stripe-band"></div>
  </section>

  <section class="envelope envelope-back" aria-label="Envelope back">
    <svg width="540" height="270" viewBox="0 0 540 270">
      <path class="flap" d="M0 0 H540 V150 Q540 160 530 158 C420 140 360 110 270 110 C180 110 120 140 10 158 Q0 160 0 150 Z" fill="var(--navy)"/>
      <circle class="flap-seal" cx="270" cy="70" r="26" fill="none" stroke="#ffffff" stroke-width="1.5"/>
    </svg>
  </section>

</body>
</html>
```